Brightmoor Cleaning Services

need a brochure for my cleaning company. Contact info coming soon .

Target Market(s)

Cleaning Services

Industry/Entity Type

Cleaning Service

Requirements
Must have
• I attached logo for you to use.

Corporate address -
472 Kestrel Ridge Way, Unit 518
Marlow Falls, OR 97351

Phone number - 877-514-SHINE
Nice to have
• bifold brochure. I attached some samples
Should not have
• Pictures of people. Keep it clean and professional.

```html
<!DOCTYPE html>
<html lang="en">
<head>
<meta charset="utf-8">
<title>Brightmoor Cleaning Services – Bifold Brochure</title>
<link href="https://fonts.googleapis.com/css2?family=Titillium+Web:ital,wght@0,700;0,900;1,700&family=Open+Sans:wght@400;700&display=swap" rel="stylesheet">
<style>
  :root {
    --brand-blue: #0a6bb8;
    --deep-blue: #0b4f93;
    --brand-red: #d8202a;
    --ink: #1e2430;
    --paper: #ffffff;
    --paper-shade: #eceef1;
    --title-grey: #e4e7ec;
    --stage: #e3e4e6;
  }
  * { margin: 0; padding: 0; box-sizing: border-box; }
  html, body { width: 931px; height: 1200px; overflow: hidden; background: var(--stage); }
  .canvas { position: relative; width: 931px; height: 1200px; }
  .spread { position: absolute; left: 130px; width: 672px; height: 540px; overflow: hidden; background: var(--paper); }
  .spread--inside { top: 40px; }
  .spread--outside { top: 622px; background: var(--brand-blue); }
  .spread > svg.backdrop { position: absolute; inset: 0; width: 672px; height: 540px; }
  .fold { position: absolute; top: 0; left: 336px; width: 1px; height: 540px; background: rgba(0,0,0,0.08); }

  .heading {
    position: absolute; font-family: "Titillium Web", sans-serif; font-weight: 700; font-style: italic;
    color: var(--ink); white-space: nowrap; line-height: 1;
  }
  .heading::after {
    content: ""; position: absolute; left: 0; bottom: -4px; height: 2px; width: 100%;
    background: linear-gradient(90deg, var(--brand-red), var(--brand-red) 70%, rgba(216,32,42,0));
  }
  .body-copy {
    position: absolute; font-family: "Open Sans", sans-serif; font-size: 6.8px; line-height: 9.3px; color: var(--ink);
  }

  /* inside spread */
  .mission-title { left: 205px; top: 58px; font-size: 13px; }
  .mission-copy { left: 205px; top: 78px; width: 112px; }
  .vision-title { left: 205px; top: 232px; font-size: 13px; }
  .vision-copy { left: 205px; top: 254px; width: 112px; }

  .offer-title { left: 353px; top: 56px; font-size: 17px; }
  .offer-intro { left: 353px; top: 84px; width: 230px; }
  .service { position: absolute; left: 353px; width: 300px; }
  .service svg { position: absolute; left: 0; top: 4px; width: 26px; height: 26px; }
  .service h3 {
    position: absolute; left: 38px; top: 0; font-family: "Titillium Web", sans-serif; font-weight: 700; font-style: italic;
    font-size: 13px; line-height: 1; color: var(--brand-blue); white-space: nowrap;
  }
  .service p { left: 38px; top: 17px; width: 260px; }
  .service--green { top: 120px; }
  .service--flexible { top: 167px; }
  .service--residential { top: 216px; }
  .service--commercial { top: 261px; }

  .brand-mark {
    position: absolute; font-family: "Titillium Web", sans-serif; font-weight: 700; line-height: 1.05;
    color: var(--brand-blue); text-align: center;
  }
  .brand-mark--inside { right: 18px; top: 22px; font-size: 10px; width: 80px; }

  .taglines { position: absolute; left: 378px; top: 440px; }
  .tagline {
    position: relative; padding-left: 17px; font-family: "Titillium Web", sans-serif; font-weight: 700; font-style: italic;
    font-size: 17px; line-height: 23px; color: var(--paper);
  }
  .tagline svg { position: absolute; left: 0; top: 3px; width: 14px; height: 14px; }

  /* outside spread */
  .testimonials-title {
    position: absolute; left: 42px; top: 20px; font-family: "Titillium Web", sans-serif; font-weight: 700; font-style: italic;
    font-size: 17px; letter-spacing: 9px; color: var(--paper); line-height: 1;
  }
  .testimonials-rule { position: absolute; left: 42px; top: 44px; width: 235px; height: 2px;
    background: linear-gradient(90deg, var(--brand-red), var(--brand-red) 75%, rgba(216,32,42,0)); }
  .testimonial { position: absolute; left: 20px; width: 240px; }
  .testimonial--one { top: 54px; }
  .testimonial--two { top: 110px; }
  .testimonial .quote-mark {
    position: absolute; left: 0; top: -4px; font-family: "Titillium Web", sans-serif; font-weight: 700; font-style: italic;
    font-size: 20px; color: var(--paper-shade); line-height: 1;
  }
  .testimonial .body-copy { position: relative; margin-left: 21px; color: var(--paper); display: block; }
  .testimonial .author {
    position: relative; display: block; margin-left: 170px; margin-top: 2px; font-family: "Open Sans", sans-serif;
    font-weight: 700; font-size: 6.8px; color: var(--paper);
  }

  .brand-mark--back { left: 215px; top: 376px; font-size: 11px; color: var(--paper); text-align: left; padding-left: 16px; }
  .brand-mark--back::before {
    content: ""; position: absolute; left: 0; top: 5px; width: 11px; height: 11px; border-radius: 50%; background: var(--paper);
  }
  .contact-title { left: 188px; top: 423px; font-size: 16px; color: var(--paper); }
  .contact-list { position: absolute; left: 178px; top: 448px; list-style: none; font-family: "Open Sans", sans-serif; font-size: 8px; line-height: 11.5px; color: var(--paper); }
  .contact-list li { position: relative; padding-left: 12px; }
  .contact-list svg { position: absolute; left: 0; top: 2px; width: 7px; height: 7px; }
  .contact-list .phone { font-weight: 700; }

  .brand-mark--front { left: 352px; top: 26px; font-size: 16px; color: var(--paper); text-align: left; }
  .cover-kicker {
    position: absolute; left: 376px; top: 350px; font-family: "Titillium Web", sans-serif; font-weight: 700; font-style: italic;
    font-size: 16px; color: var(--title-grey); white-space: nowrap; line-height: 1;
  }
  .cover-title {
    position: absolute; left: 372px; top: 370px; font-family: "Titillium Web", sans-serif; font-weight: 900;
    font-size: 50px; line-height: 44px; color: var(--title-grey); letter-spacing: 0.5px;
  }
</style>
</head>
<body>
<main class="canvas">

  <section class="spread spread--inside">
    <svg class="backdrop" viewBox="0 0 672 540">
      <defs>
        <linearGradient id="interiorTone" x1="0" y1="0" x2="1" y2="1">
          <stop offset="0" stop-color="#c9a98a"/>
          <stop offset="0.45" stop-color="#b8b0a6"/>
          <stop offset="1" stop-color="#9a9590"/>
        </linearGradient>
        <linearGradient id="doorTone" x1="0" y1="0" x2="1" y2="0">
          <stop offset="0" stop-color="#e2e1de"/>
          <stop offset="1" stop-color="#f4f4f2"/>
        </linearGradient>
        <linearGradient id="paperTone" x1="0" y1="0" x2="1" y2="0">
          <stop offset="0" stop-color="#e7e8ea"/>
          <stop offset="0.3" stop-color="#ffffff"/>
        </linearGradient>
        <linearGradient id="wipeTone" x1="0" y1="0" x2="1" y2="1">
          <stop offset="0" stop-color="#e9eef4"/>
          <stop offset="0.5" stop-color="#e8c24a"/>
          <stop offset="1" stop-color="#e6d8c4"/>
        </linearGradient>
        <linearGradient id="carpetTone" x1="0" y1="0" x2="1" y2="1">
          <stop offset="0" stop-color="#e6dccc"/>
          <stop offset="1" stop-color="#cbb9a0"/>
        </linearGradient>
      </defs>
      <rect x="336" y="0" width="336" height="540" fill="url(#paperTone)"/>
      <g role="img" aria-label="Softly blurred bright living room interior with a lamp and a doorway">
        <rect x="0" y="0" width="336" height="540" fill="url(#interiorTone)"/>
        <rect x="185" y="0" width="151" height="540" fill="url(#doorTone)"/>
      </g>
      <path d="M0,440 C120,470 220,480 336,440 C440,405 560,360 672,340 L672,350 C560,370 440,415 336,452 C220,492 120,486 0,450 Z" fill="var(--brand-red)"/>
      <path d="M0,472 C120,500 220,505 336,460 C440,420 560,372 672,354 L672,540 L0,540 Z" fill="var(--brand-blue)"/>
      <path d="M0,466 C120,496 220,500 336,455 C440,416 560,368 672,350" fill="none" stroke="#ffffff" stroke-width="2"/>
      <g role="img" aria-label="Gloved hand wiping a surface with a blue cloth and a spray bottle">
        <circle cx="99" cy="438" r="78" fill="url(#wipeTone)" stroke="var(--brand-blue)" stroke-width="3"/>
      </g>
      <g role="img" aria-label="Close-up of a carpet being cleaned with a steam wand">
        <circle cx="590" cy="360" r="60" fill="url(#carpetTone)" stroke="var(--brand-blue)" stroke-width="3"/>
      </g>
    </svg>
    <div class="fold"></div>

    <h2 class="heading mission-title">OUR MISSION</h2>
    <p class="body-copy mission-copy">Lorem ipsum dolor sit amet, consectetur adipiscing elit, sed do eiusmod tempor incididunt ut labore et dolore magna aliqua. Ut enim ad minim veniam, quis nostrud exercitation ullamco laboris nisi ut aliquip ex ea commodo consequat. Duis aute irure dolor in reprehenderit in voluptate velit esse cillum dolore eu fugiat nulla pariatur. Excepteur sint occaecat cupidatat non proident, sunt in culpa qui officia deserunt mollit anim id est laborum.</p>
    <h2 class="heading vision-title">OUR VISION</h2>
    <p class="body-copy vision-copy">Lorem ipsum dolor sit amet, consectetur adipiscing elit, sed do eiusmod tempor incididunt ut labore et dolore magna aliqua. Ut enim ad minim veniam, quis nostrud exercitation ullamco laboris nisi ut aliquip ex ea commodo consequat. Duis aute irure dolor in reprehenderit in voluptate velit esse cillum dolore eu fugiat nulla pariatur. Excepteur sint occaecat cupidatat non proident, sunt in culpa qui officia deserunt mollit anim id est laborum.</p>

    <div class="brand-mark brand-mark--inside">Brightmoor Cleaning Services</div>

    <h2 class="heading offer-title">THE SERVICE WE OFFER</h2>
    <p class="body-copy offer-intro">Lorem ipsum dolor sit amet, consectetur adipiscing elit, sed do eiusmod tempor incididunt ut labore et dolore magna aliqua.</p>

    <article class="service service--green">
      <svg viewBox="0 0 26 26" fill="none" stroke="var(--deep-blue)" stroke-width="1.4"><path d="M4 10 L13 6 L22 10 L22 20 L13 24 L4 20 Z M4 10 L13 14 L22 10 M13 14 L13 24"/></svg>
      <h3>GREEN PRODUCTS</h3>
      <p class="body-copy">Lorem ipsum dolor sit amet, consectetur adipiscing elit, sed do eiusmod tempor incididunt ut labore et dolore magna aliqua.</p>
    </article>
    <article class="service service--flexible">
      <svg viewBox="0 0 26 26"><circle cx="13" cy="13" r="12" fill="var(--deep-blue)"/><circle cx="13" cy="13" r="8.5" fill="none" stroke="#fff" stroke-width="1.2"/><path d="M13 8 L13 13 L17 15" fill="none" stroke="#fff" stroke-width="1.4"/></svg>
      <h3>FLEXIBLE SCHEDULING</h3>
      <p class="body-copy">Lorem ipsum dolor sit amet, consectetur adipiscing elit, sed do eiusmod tempor incididunt ut labore et dolore magna aliqua.</p>
    </article>
    <article class="service service--residential">
      <svg viewBox="0 0 26 26"><path d="M2 12 L13 4 L24 12 L22 12 L22 23 L4 23 L4 12 Z" fill="var(--deep-blue)"/><rect x="8" y="15" width="4" height="4" fill="#fff"/><rect x="14" y="15" width="4" height="4" fill="#fff"/></svg>
      <h3>RESIDENTIAL</h3>
      <p class="body-copy">Lorem ipsum dolor sit amet, consectetur adipiscing elit, sed do eiusmod tempor incididunt ut labore et dolore magna aliqua.</p>
    </article>
    <article class="service service--commercial">
      <svg viewBox="0 0 26 26"><rect x="3" y="9" width="10" height="15" fill="var(--deep-blue)"/><rect x="12" y="3" width="11" height="21" fill="var(--deep-blue)"/><g fill="#fff"><rect x="5" y="12" width="2" height="2"/><rect x="9" y="12" width="2" height="2"/><rect x="5" y="17" width="2" height="2"/><rect x="9" y="17" width="2" height="2"/><rect x="15" y="7" width="2" height="2"/><rect x="19" y="7" width="2" height="2"/><rect x="15" y="12" width="2" height="2"/><rect x="19" y="12" width="2" height="2"/><rect x="15" y="17" width="2" height="2"/><rect x="19" y="17" width="2" height="2"/></g></svg>
      <h3>COMMERCIAL</h3>
      <p class="body-copy">Lorem ipsum dolor sit amet, consectetur adipiscing elit, sed do eiusmod tempor incididunt ut labore et dolore magna aliqua.</p>
    </article>

    <div class="taglines">
      <p class="tagline"><svg viewBox="0 0 14 14"><path d="M1 7 L5 12 L13 1" fill="none" stroke="var(--brand-red)" stroke-width="2"/></svg>We like when it’s clean around!</p>
      <p class="tagline"><svg viewBox="0 0 14 14"><path d="M1 7 L5 12 L13 1" fill="none" stroke="var(--brand-red)" stroke-width="2"/></svg>We working hard to make<br>your place clean</p>
    </div>
  </section>

  <section class="spread spread--outside">
    <svg class="backdrop" viewBox="0 0 672 540">
      <defs>
        <linearGradient id="bandTone" x1="0" y1="1" x2="1" y2="0">
          <stop offset="0" stop-color="#c8c3bc"/>
          <stop offset="0.45" stop-color="#e2ddd6"/>
          <stop offset="0.7" stop-color="#6a8fc0"/>
          <stop offset="1" stop-color="#d7c8a0"/>
        </linearGradient>
      </defs>
      <g role="img" aria-label="Bright hallway with a bucket of colourful cleaning supplies">
        <path d="M0,381 C100,270 200,195 336,133 C450,95 560,70 672,51 L672,285 C560,290 440,300 336,318 C270,330 210,360 170,420 C140,465 115,505 103,540 L0,540 Z" fill="url(#bandTone)"/>
      </g>
      <path d="M0,381 C100,270 200,195 336,133 C450,95 560,70 672,51" fill="none" stroke="#fff" stroke-width="4"/>
      <path d="M672,285 C560,290 440,300 336,318 C270,330 210,360 170,420 C140,465 115,505 103,540" fill="none" stroke="#fff" stroke-width="4"/>
    </svg>
    <div class="fold"></div>

    <h2 class="testimonials-title">TESTIMONIALS</h2>
    <div class="testimonials-rule"></div>
    <blockquote class="testimonial testimonial--one">
      <span class="quote-mark">“</span>
      <span class="body-copy">Lorem ipsum dolor sit amet, consectetur adipiscing elit, sed do eiusmod tempor incididunt ut labore et dolore magna aliqua. Ut enim ad minim veniam, quis nostrud exercitation ullamco laboris nisi ut aliquip ex ea commodo consequat.</span>
      <cite class="author">-Dana Whitfield</cite>
    </blockquote>
    <blockquote class="testimonial testimonial--two">
      <span class="quote-mark">“</span>
      <span class="body-copy">Lorem ipsum dolor sit amet, consectetur adipiscing elit, sed do eiusmod tempor incididunt ut labore et dolore magna aliqua. Ut enim ad minim veniam, quis nostrud exercitation ullamco laboris nisi ut aliquip ex ea commodo consequat.</span>
      <cite class="author">-Dana Whitfield</cite>
    </blockquote>

    <div class="brand-mark brand-mark--back">Brightmoor<br>Cleaning Services</div>
    <h2 class="heading contact-title">CONTACT US</h2>
    <ul class="contact-list">
      <li><svg viewBox="0 0 8 8"><path d="M4 8 L1 4 A3 3 0 1 1 7 4 Z" fill="var(--brand-red)"/></svg>472 Kestrel Ridge Way, Unit 518</li>
      <li>Marlow Falls, OR 97351</li>
      <li class="phone"><svg viewBox="0 0 8 8"><path d="M1 1 L3 1 L4 3 L3 4 Q4 5.5 5 5 L7 5 L7 7 Q2 7.5 1 1 Z" fill="var(--brand-red)"/></svg>877-514-SHINE</li>
      <li><svg viewBox="0 0 8 8"><rect x="0.5" y="1.5" width="7" height="5" fill="var(--brand-red)"/><path d="M0.5 1.5 L4 4.5 L7.5 1.5" fill="none" stroke="#fff" stroke-width="0.7"/></svg>info@brightmoorcleaning.com</li>
    </ul>

    <div class="brand-mark brand-mark--front">Brightmoor<br>Cleaning Services</div>
    <p class="cover-kicker">RESIDENTIAL &amp; COMMERCIAL</p>
    <h1 class="cover-title">CLEANING<br>SERVICES</h1>
  </section>

</main>
</body>
</html>
```